Lumara Health & Wellness Business Card Design

We would like to create business cards matching with our new logo design. The card should be professional looking but still have a playful side and something that would be eye catching. We are planing to open a luxury medical spa and looking to create a design based on this new logo. We are looking for a design that shows off luxury but not be gold in color. Also, while we are a more female oriented medical center we do have men that come in for our services and it should be be too feminine.

Target Market(s)

Health & Wellness. Medical patients. Luxury spa

Industry/Entity Type

Health And Wellness

Contact Information for Business Card

It should have the logo design in the front of card and back of card should have our contact information. Our current colors are peach/ coral, teal, and gray. We are looking for a modern looking design.

Font styles to use
Script

Colors
32a6d6
e667a6
86cfc6
fece3e

Requirements
Must have
• It should have our logo design. We would prefer to have a more modern look to the card.
Nice to have
• Eye-Catching Design on the personable side but still classy.
Should not have
• At this point we are looking for the best design. It should not have color purple.

```html
<!DOCTYPE html>
<html lang="en">
<head>
<meta charset="UTF-8">
<title>Lumara Health &amp; Wellness – Business Card</title>
<link href="https://fonts.googleapis.com/css2?family=Open+Sans:wght@400;600&display=swap" rel="stylesheet">
<style>
  :root{
    --bg:#ececec;
    --pink:#ea7ab1;
    --pink-light:#ee8dbd;
    --pink-band:#e86fae;
    --blue:#32a6d6;
    --blue-light:#5fb9e3;
    --ink:#1e1e1e;
    --muted:#555;
    --white:#ffffff;
  }
  *{margin:0;padding:0;box-sizing:border-box}
  html,body{width:1200px;height:1200px;overflow:hidden;background:var(--bg)}
  body{font-family:"Open Sans",sans-serif;display:flex;flex-direction:column;align-items:center;justify-content:center;gap:60px}
  .card{width:900px;height:514px;position:relative;overflow:hidden;box-shadow:0 6px 18px rgba(0,0,0,.12)}
  .card--front{background:linear-gradient(120deg,var(--pink) 0%,var(--pink-light) 45%,var(--pink) 70%,var(--pink-light) 100%);display:flex;align-items:center;justify-content:center}
  .brand{font-weight:600;letter-spacing:.04em;text-align:center;line-height:1.25}
  .card--front .brand{color:var(--white);font-size:46px}
  .card--back{background:var(--white)}
  .card--back .brand{position:absolute;left:250px;top:90px;color:var(--ink);font-size:30px;text-align:left}
  .person{position:absolute;left:140px;top:210px}
  .person__name{font-size:30px;font-weight:600;color:var(--ink)}
  .person__role{font-size:18px;color:var(--muted);margin-top:2px}
  .contact{position:absolute;left:470px;top:300px;list-style:none;font-size:21px;color:var(--ink);line-height:1.55}
  .contact li{display:flex;align-items:center;gap:14px}
  .contact svg{width:18px;height:18px;flex:none}
  .band{position:absolute;left:0;right:0;bottom:0;height:26px;display:flex}
  .band__pink{width:45%;background:var(--pink-band)}
  .band__blue{flex:1;background:linear-gradient(90deg,var(--blue),var(--blue-light))}
</style>
</head>
<body>
  <section class="card card--front">
    <p class="brand">Lumara Health &amp; Wellness</p>
  </section>

  <section class="card card--back">
    <p class="brand">Lumara Health &amp; Wellness</p>
    <div class="person">
      <p class="person__name">Maren Ellison</p>
      <p class="person__role">Founder</p>
    </div>
    <ul class="contact">
      <li>
        <svg viewBox="0 0 20 20" aria-hidden="true"><path d="M5 2c1 0 2 3 2 4s-1.5 1.5-1 3 2.5 4 4 4.5 2-1 3-1 4 1 4 2-2 3-3.5 3C8 17.5 2.5 12 2.5 5.5 2.5 4 4 2 5 2z" fill="#777"/></svg>
        (000) 000-0000
      </li>
      <li>
        <svg viewBox="0 0 20 20" aria-hidden="true"><rect x="2" y="4.5" width="16" height="11" fill="none" stroke="#777" stroke-width="1.4"/><path d="M2 4.5l8 6 8-6" fill="none" stroke="#777" stroke-width="1.4"/></svg>
        name@email.com
      </li>
      <li>
        <svg viewBox="0 0 20 20" aria-hidden="true"><path d="M8.5 11.5l3-3M7 9l-2 2a2.8 2.8 0 004 4l2-2M13 11l2-2a2.8 2.8 0 00-4-4l-2 2" fill="none" stroke="#777" stroke-width="1.5" stroke-linecap="round"/></svg>
        www.domain.com
      </li>
    </ul>
    <div class="band"><span class="band__pink"></span><span class="band__blue"></span></div>
  </section>
</body>
</html>
```